Coffee Bag Design for Tidewell Coffee

We’re excited to invite you to help us bring Tidewell Coffee to life on grocery store shelves with a design that embodies our mission of spreading goodness and creating a lasting impact. Tidewell Coffee represents warmth, positivity, and the power of small actions to create ripples of goodness. Each cup not only offers a rich, gourmet coffee experience but also gives back to the community, with $2 from each bag supporting local food banks.

To reflect this vision, we’d love for the design to feature a dark (greyish) blue as the base color to convey depth and quality, complemented by a vibrant light blue that will catch the eye and add energy. Tan or gold accents could add an elegant touch and a feeling of warmth. We are aiming for a look that feels uplifting and engaging, with simplicity and elegance, yet stands out amid other brands on the shelf.

I am attaching the dimension of the bag.

Other information that needs to be listed:
Ingredients: 100% Arabica Coffee
Net Wt. 12 oz. (340 g)
Roasted and distributed by:
Name
Address
email

Text on the back of the bag:
Tidewell Coffee is crafted with a belief that kindness and positivity can spread, touching countless lives with every sip. This gourmet blend delivers a rich taste experience while giving back, as $2 from each bag sold is donated to local food banks to help those in need. Enjoy the warmth and goodness in each cup, knowing you’re making a difference with every purchase.

Thank you!

```html
<!DOCTYPE html>
<html lang="en">
<head>
<meta charset="utf-8">
<title>Tidewell Coffee – Bag Dieline</title>
<link rel="stylesheet" href="https://fonts.googleapis.com/css2?family=Exo+2:wght@400;600;700&display=swap">
<style>
  :root{
    --paper:#ffffff;
    --sky:#6396ff;
    --ink-line:#1c2340;
    --stripe-dark:#434363;
    --stripe-light:#58587c;
    --gold:#d39b2e;
    --guide:#b03aa8;
    --dim:#2c56a3;
    --label:#8b2f8f;
    --seal:#cfcfcf;
  }
  *{box-sizing:border-box;margin:0;padding:0}
  html,body{width:1200px;height:795px;overflow:hidden;background:var(--paper)}
  .sheet{position:relative;width:1200px;height:795px;border:1px solid #555;font-family:"Exo 2",sans-serif}
  .panel-label{position:absolute;top:99px;font-size:11.5px;color:var(--label);transform:translateX(-50%)}
  .panel{position:absolute;background:var(--sky);border:1px solid var(--ink-line);border-radius:9px;overflow:hidden}
  .panel--left{left:76px;top:134px;width:182px;height:410px}
  .panel--front{left:258px;top:134px;width:342px;height:410px}
  .panel--right{left:600px;top:134px;width:183px;height:410px}
  .panel--back{left:783px;top:134px;width:342px;height:410px}
  .panel--gusset{left:258px;top:545px;width:342px;height:181px}
  .trim-guide{position:absolute;top:4px;bottom:15px;left:14px;right:14px;border:1px dashed var(--guide);border-top:none}
  .gusset-guide{position:absolute;left:19px;right:9px;top:14px;bottom:14px;border:1px dashed #333}
  .cup-pattern{position:absolute;inset:0}
  .stripe-field{position:absolute;top:0;bottom:0;left:51px;width:240px;
    background:repeating-linear-gradient(90deg,var(--stripe-dark) 0 21.8px,var(--stripe-light) 21.8px 43.6px)}
  .gold-bar{position:absolute;top:0;bottom:0;width:9px;background:var(--gold)}
  .panel--front .gold-bar--a{left:42px}
  .panel--front .gold-bar--b{left:291px}
  .panel--back .gold-bar--a{left:41px}
  .panel--back .gold-bar--b{left:290px}
  .panel--back .stripe-field{left:50px;width:240px}
  .brand-name{position:absolute;left:0;right:0;top:142px;text-align:center;font-size:25px;font-weight:700;color:var(--gold);letter-spacing:-0.5px}
  .cup-art{position:absolute;left:116px;top:174px;width:111px;height:142px;border-radius:40% 40% 45% 45%;
    background:radial-gradient(ellipse at 50% 70%,rgba(211,155,46,.45),rgba(211,155,46,.12))}
  .blend{position:absolute;left:186px;width:110px;text-align:center;color:var(--gold);font-weight:700}
  .blend__pct{top:339px;font-size:17px;line-height:1;letter-spacing:0.3px}
  .blend__kind{top:357px;font-size:8px;font-weight:600;letter-spacing:0.4px}
  .net-weight{position:absolute;left:186px;width:110px;text-align:center;top:382px;font-size:7.5px;font-weight:600;letter-spacing:0.3px;color:var(--gold);white-space:nowrap}
  .roaster{position:absolute;left:58px;top:360px;font-size:7.5px;font-weight:600;line-height:9px;letter-spacing:0.4px;color:var(--gold)}
  .seal-spot{position:absolute;left:145px;top:159px;width:50px;height:50px;border-radius:50%;background:var(--seal)}
  .zip-tab{position:absolute;left:1px;top:48px;width:17px;height:40px;border-radius:8px;background:rgba(215,215,230,.6)}
  .zip-line{position:absolute;left:21px;right:0;height:2px;background:rgba(225,225,235,.8)}
  .zip-line--1{top:67px}
  .zip-line--2{top:78px;height:1px;background:rgba(200,205,225,.5)}
  .zip-band{position:absolute;left:21px;right:0;top:86px;height:7px;background:rgba(190,195,225,.45)}
  .story{position:absolute;left:30px;right:30px;top:236px;text-align:center;font-size:13.8px;font-weight:700;line-height:16.7px;letter-spacing:0.8px;color:var(--gold);white-space:nowrap}
  .dims{position:absolute;left:0;top:0}
  .dim-text{position:absolute;left:40px;top:352px;width:50px;text-align:center;white-space:nowrap;font-size:11.5px;line-height:14px;color:var(--dim);transform:rotate(-90deg);transform-origin:center;z-index:2}
</style>
</head>
<body>
<div class="sheet">
  <span class="panel-label" style="left:171px">Left</span>
  <span class="panel-label" style="left:456px">Front</span>
  <span class="panel-label" style="left:690px">Right</span>
  <span class="panel-label" style="left:924px">Back</span>

  <svg class="dims" width="1200" height="795" aria-hidden="true">
    <g stroke="var(--dim)" stroke-width="1" fill="none">
      <line x1="76" y1="122" x2="1124" y2="122"/>
      <line x1="76" y1="116" x2="76" y2="138"/>
      <line x1="258" y1="116" x2="258" y2="130"/><line x1="253" y1="118" x2="263" y2="126"/><line x1="253" y1="126" x2="263" y2="118"/>
      <line x1="600" y1="116" x2="600" y2="130"/><line x1="595" y1="118" x2="605" y2="126"/><line x1="595" y1="126" x2="605" y2="118"/>
      <line x1="783" y1="116" x2="783" y2="130"/><line x1="778" y1="118" x2="788" y2="126"/><line x1="778" y1="126" x2="788" y2="118"/>
      <line x1="1122" y1="116" x2="1122" y2="140"/>
      <polyline points="82,118 76,122 82,126"/>
      <polyline points="1116,118 1122,122 1116,126"/>
      <line x1="57" y1="134" x2="1151" y2="134"/>
      <line x1="57" y1="544" x2="120" y2="544"/>
      <line x1="63" y1="134" x2="63" y2="330"/>
      <line x1="63" y1="378" x2="63" y2="550"/>
      <polyline points="59,140 63,134 67,140"/>
      <polyline points="59,538 63,544 67,538"/>
    </g>
  </svg>
  <span class="dim-text">180 mm</span>

  <section class="panel panel--left">
    <div class="cup-pattern" role="img" aria-label="Repeating pattern of small steaming coffee cups"></div>
    <div class="trim-guide"></div>
  </section>

  <section class="panel panel--front">
    <div class="cup-pattern" role="img" aria-label="Repeating pattern of small steaming coffee cups"></div>
    <div class="trim-guide"></div>
    <div class="stripe-field"></div>
    <div class="gold-bar gold-bar--a"></div>
    <div class="gold-bar gold-bar--b"></div>
    <h1 class="brand-name">Tidewell Coffee</h1>
    <div class="cup-art" role="img" aria-label="Gold line illustration of a steaming coffee cup on a saucer"></div>
    <p class="blend blend__pct">100%</p>
    <p class="blend blend__kind">Arabica Coffee</p>
    <p class="roaster">Roasted and distributed by:<br>Name<br>Address<br>email</p>
    <p class="net-weight">Net Wt. 12 oz. (340g)</p>
  </section>

  <section class="panel panel--right">
    <div class="cup-pattern" role="img" aria-label="Repeating pattern of small steaming coffee cups"></div>
    <div class="trim-guide"></div>
  </section>

  <section class="panel panel--back">
    <div class="trim-guide"></div>
    <div class="stripe-field"></div>
    <div class="gold-bar gold-bar--a"></div>
    <div class="gold-bar gold-bar--b"></div>
    <div class="zip-tab"></div>
    <div class="zip-line zip-line--1"></div>
    <div class="zip-line zip-line--2"></div>
    <div class="zip-band"></div>
    <div class="seal-spot"></div>
    <p class="story">Tidewell Coffee is crafted<br>with a belief that kindness<br>and positivity can spread,<br>touching countless lives with<br>every sip. This gourmet<br>blend delivers a rich taste<br>experience while giving<br>back, as $2 from each bag</p>
  </section>

  <section class="panel panel--gusset">
    <div class="gusset-guide"></div>
  </section>
</div>
</body>
</html>
```